Buch-/E-Book-Cover für Schriftstellerin
Vielen Dank für das schöne Cover zu meiner Kurzgeschichtensammlung!
Zielgruppe
30-jährige Schriftstellerin (Kurzgeschichten, Roman in Arbeit, Gedichte)
Zielgruppe der Kurzgeschichtensammlung 'Sofawirbel': 17-50 Jährige Kurzgeschichten-Leser (alle Geschlechter), Tomio Sadakawa-, Brackwater-, Lodur-Leser, Hobby-Philosophen, Intellektuelle, Melancholiker
Klappentext:
„Miese Gedanken sind der Isolierstoff zwischen mir und meiner Umwelt.“
Eine Frau geht in ihrer Badewanne an Bord eines Papierschiffs, ein Paar wandert über Möbel und ein Mann, dessen Name sich keiner merken kann, spricht von der Couch aus mit seinen Bücherschränken...
„Sofawirbel“ nähert sich dem modernen Menschen auf einfühlsame wie humoristische Weise. Psychologisch, verträumt, surreal und wohltuend melancholisch - in 14 Kurzgeschichten treffen Personen und Mobiliar, Seelenraum und Außenwelt, Pandemie und Heavy Metal aufeinander.
Aufgabenstellung
Design passend zum Titel 'Sofawirbel'. In meiner Geschichte ist das Sofawirbel der Moment, in dem der depressive und angstgeplagte Protagonist auf der Couch liegt und sich das Chaos vorstellt, das er anrichten würde, wenn er die Möbel auf den Kopf stellen würde, sodass die Schubladen der Schränke keinen Sinn mehr ergäben oder er seinen Körper aufschneiden würde. Die Geschichte hat ein Happy End und er wird gesund. Es ist nur ein kurzer Moment der Depression. Die 14 Kurzgeschichten sind nachenklich, ehrlich, aber auch stellenweise lustig sowie surreal.
Das Cover soll farbenfroh sein und mit serifenloser Schrift, abstrakt-künstlerisch und modern. Bitte keine Fotos von 'realen' Menschen.
Titel: Sofawirbel (kann auch großgeschrieben sein)
Untertitel: 14 Kurzgeschichten
Autorin: Marlene Tieck
Ansonsten keine Vorgaben.

```html
<!DOCTYPE html>
<html lang="de">
<head>
<meta charset="utf-8">
<title>Sofawirbel – Marlene Tieck</title>
<link rel="stylesheet" href="https://fonts.googleapis.com/css2?family=Bebas+Neue&family=Oswald:wght@400;500&display=swap">
<style>
  :root {
    --paper: #ffffff;
    --ink-blue: #1a14b4;
    --signal-orange: #ff4a12;
    --sun-yellow: #ffbe14;
    --deep-black: #0c0f14;
    --title-white: #fafafa;
  }
  html, body {
    margin: 0;
    padding: 0;
    overflow: hidden;
    background: var(--paper);
  }
  .cover {
    position: relative;
    width: 750px;
    height: 1200px;
    overflow: hidden;
    background: var(--paper);
  }
  .cover-art {
    position: absolute;
    inset: 0;
    width: 750px;
    height: 1200px;
  }
  .book-title {
    position: absolute;
    left: 112px;
    top: 440px;
    margin: 0;
    font-family: "Bebas Neue", "Oswald", sans-serif;
    font-weight: 400;
    font-size: 236px;
    line-height: 184px;
    letter-spacing: 2px;
    color: var(--title-white);
    text-shadow: 6px 8px 12px rgba(0, 0, 0, 0.45);
  }
  .book-title span { display: block; }
  .subtitle {
    position: absolute;
    left: 682px;
    top: 384px;
    margin: 0;
    transform: rotate(-90deg);
    transform-origin: 0 0;
    font-family: "Oswald", sans-serif;
    font-weight: 500;
    font-size: 43px;
    line-height: 40px;
    white-space: nowrap;
    color: var(--ink-blue);
    letter-spacing: 0.5px;
  }
  .author {
    position: absolute;
    right: 32px;
    top: 1118px;
    margin: 0;
    font-family: "Oswald", sans-serif;
    font-weight: 400;
    font-size: 58px;
    line-height: 60px;
    white-space: nowrap;
    color: var(--signal-orange);
  }
</style>
</head>
<body>
<main class="cover">
  <svg class="cover-art" viewBox="0 0 750 1200" role="img" aria-label="Abstrakte geometrische Komposition aus Streifen, Bögen, Dreiecken und Kreisen in Blau, Orange, Gelb und Schwarz">
    <defs>
      <linearGradient id="art-tones" x1="0" y1="0" x2="1" y2="1">
        <stop offset="0" stop-color="var(--sun-yellow)"/>
        <stop offset="0.35" stop-color="var(--signal-orange)"/>
        <stop offset="0.65" stop-color="var(--ink-blue)"/>
        <stop offset="1" stop-color="var(--sun-yellow)"/>
      </linearGradient>
    </defs>
    <polygon fill="url(#art-tones)"
      points="200,20 470,20 470,190 550,200 550,400 650,430 660,600 750,600 750,760 660,760 660,840 520,840 520,1100 430,1100 420,1190 280,1190 280,1080 190,1080 190,840 95,840 95,760 0,760 0,640 50,640 95,390 190,390 190,100"/>
  </svg>

  <h1 class="book-title"><span>Sofa</span><span>Wirbel</span></h1>
  <p class="subtitle">14 KURZGESCHICHTEN</p>
  <p class="author">MARLENE TIECK</p>
</main>
</body>
</html>
```